Blister Packaging Design for a Mouthguard

I need a clean and professional design for a mouthguard packaging.
the design should be clean, mostly black, white and grey. it should show our logo "VORTANEL". The Frontside schould show the German word "MUNDSCHUTZ" and smaller the Term "Mouthguard". the pfont should also show some parts in german flag colors to show we are a german company. at some place there has to be a place where the different style can be inserted. 4 main styles will be: "STRGL", "SPINDLE", "GLIMMER", "NEBEL TOR"
on the backside there need to be a place for the barcode and our company adress, detailes product description an maybe a picture of a drawed mouthguard.
Attached as well a finished design from some other company, just to show where the mouthguard will be placed in the packaging.
Target Market(s)
Boxing and Fighting sports in general
Industry/Entity Type
sport, fighting sports
Colors
Designer to choose only greyscale colors for use in the design.
Requirements
Must have
- clean and professional design
Nice to have
- German flag/Colors somewhere embedded on the front of the packaging
Should not have
- not too colorful

```html
<!DOCTYPE html>
<html lang="de">
<head>
<meta charset="utf-8">
<title>Mundschutz Verpackung – Stilvarianten</title>
<link rel="stylesheet" href="https://fonts.googleapis.com/css2?family=Exo+2:wght@600&family=Krona+One&display=swap">
<style>
  :root {
    --page: #ffffff;
    --card-dark: #0d0d0d;
    --card-mid: #2c2c2c;
    --text-light: #ececec;
    --text-dark: #0a0a0a;
    --strgl-glow: #f6f6f6;
    --strgl-mid: #c4c4c4;
    --strgl-deep: #8a8a8a;
    --glimmer-glow: #ff6a00;
    --glimmer-mid: #d94f00;
    --glimmer-deep: #9a3a08;
    --spindle-glow: #2288ff;
    --spindle-mid: #1462cc;
    --spindle-deep: #0d3f85;
    --nebel-glow: #8fe291;
    --nebel-mid: #5bb761;
    --nebel-deep: #2f6b36;
  }
  * { box-sizing: border-box; margin: 0; padding: 0; }
  html, body {
    width: 848px; height: 1200px; overflow: hidden;
    background: var(--page);
  }
  .sheet { position: relative; width: 848px; height: 1200px; }
  .card {
    position: absolute;
    width: 317px; height: 479px;
    border-radius: 15px;
    overflow: hidden;
    background: var(--card-dark);
  }
  .card--strgl   { left: 96px;  top: 117px; }
  .card--glimmer { left: 422px; top: 117px; }
  .card--spindle { left: 95px;  top: 608px; }
  .card--nebel   { left: 420px; top: 608px; }

  .card__texture {
    position: absolute; inset: 0;
    background: radial-gradient(ellipse 70% 45% at 50% 56%, var(--card-mid) 0%, #181818 60%, var(--card-dark) 100%);
  }
  .card__band { position: absolute; inset: 0; width: 100%; height: 100%; }

  .brand {
    position: absolute; top: 70px; left: 0; right: 0;
    display: flex; align-items: center; justify-content: center; gap: 8px;
    font-family: "Exo 2", sans-serif; font-weight: 600;
    font-size: 20px; line-height: 1; letter-spacing: 1.5px;
    color: var(--text-light);
  }
  .brand__mark { width: 13px; height: 13px; background: var(--text-light); }
  .title {
    position: absolute; top: 127px; left: 0; right: 0;
    text-align: center;
    font-family: "Exo 2", sans-serif; font-weight: 600;
    font-size: 27px; line-height: 1; letter-spacing: 0.3px;
    color: var(--text-light);
  }
  .subtitle {
    position: absolute; top: 155px; left: 0; right: 0;
    text-align: center;
    font-family: "Krona One", sans-serif;
    font-size: 11px; line-height: 1; letter-spacing: 0.6px;
    color: var(--text-light);
  }
  .style-name {
    position: absolute; right: 20px; bottom: 17px;
    font-family: "Krona One", sans-serif;
    font-size: 23px; line-height: 1; letter-spacing: 0.3px;
    color: var(--text-light);
    white-space: nowrap;
  }
  .card--strgl .style-name { color: var(--text-dark); }
</style>
</head>
<body>
<main class="sheet">

  <section class="card card--strgl">
    <div class="card__texture" role="img" aria-label="Dunkles Wabenmuster als Hintergrund"></div>
    <svg class="card__band" viewBox="0 0 317 479" aria-hidden="true">
      <defs>
        <radialGradient id="glow-strgl" gradientUnits="userSpaceOnUse" cx="205" cy="420" r="170">
          <stop offset="0" stop-color="var(--strgl-glow)"/>
          <stop offset="0.55" stop-color="var(--strgl-mid)"/>
          <stop offset="1" stop-color="#3a3a3a"/>
        </radialGradient>
      </defs>
      <polygon points="58,479 317,326 317,479" fill="var(--strgl-deep)" opacity="0.5"/>
      <polygon points="66,479 317,350 317,479" fill="url(#glow-strgl)"/>
    </svg>
    <div class="brand"><span class="brand__mark"></span>VORTANEL</div>
    <h1 class="title">MUNDSCHUTZ</h1>
    <p class="subtitle">MOUTHGUARD</p>
    <p class="style-name">STRGL</p>
  </section>

  <section class="card card--glimmer">
    <div class="card__texture" role="img" aria-label="Dunkles Wabenmuster als Hintergrund"></div>
    <svg class="card__band" viewBox="0 0 317 479" aria-hidden="true">
      <defs>
        <radialGradient id="glow-glimmer" gradientUnits="userSpaceOnUse" cx="210" cy="425" r="170">
          <stop offset="0" stop-color="var(--glimmer-glow)"/>
          <stop offset="0.55" stop-color="var(--glimmer-mid)"/>
          <stop offset="1" stop-color="#3a1606"/>
        </radialGradient>
      </defs>
      <polygon points="58,479 317,318 317,479" fill="var(--glimmer-deep)" opacity="0.6"/>
      <polygon points="66,479 317,350 317,479" fill="url(#glow-glimmer)"/>
    </svg>
    <div class="brand"><span class="brand__mark"></span>VORTANEL</div>
    <h1 class="title">MUNDSCHUTZ</h1>
    <p class="subtitle">MOUTHGUARD</p>
    <p class="style-name">GLIMMER</p>
  </section>

  <section class="card card--spindle">
    <div class="card__texture" role="img" aria-label="Dunkles Wabenmuster als Hintergrund"></div>
    <svg class="card__band" viewBox="0 0 317 479" aria-hidden="true">
      <defs>
        <radialGradient id="glow-spindle" gradientUnits="userSpaceOnUse" cx="215" cy="425" r="170">
          <stop offset="0" stop-color="var(--spindle-glow)"/>
          <stop offset="0.55" stop-color="var(--spindle-mid)"/>
          <stop offset="1" stop-color="#0b1d38"/>
        </radialGradient>
      </defs>
      <polygon points="58,479 317,318 317,479" fill="var(--spindle-deep)" opacity="0.6"/>
      <polygon points="66,479 317,350 317,479" fill="url(#glow-spindle)"/>
    </svg>
    <div class="brand"><span class="brand__mark"></span>VORTANEL</div>
    <h1 class="title">MUNDSCHUTZ</h1>
    <p class="subtitle">MOUTHGUARD</p>
    <p class="style-name">SPINDLE</p>
  </section>

  <section class="card card--nebel">
    <div class="card__texture" role="img" aria-label="Dunkles Wabenmuster als Hintergrund"></div>
    <svg class="card__band" viewBox="0 0 317 479" aria-hidden="true">
      <defs>
        <radialGradient id="glow-nebel" gradientUnits="userSpaceOnUse" cx="190" cy="430" r="175">
          <stop offset="0" stop-color="var(--nebel-glow)"/>
          <stop offset="0.55" stop-color="var(--nebel-mid)"/>
          <stop offset="1" stop-color="#14301a"/>
        </radialGradient>
      </defs>
      <polygon points="58,479 317,318 317,479" fill="var(--nebel-deep)" opacity="0.6"/>
      <polygon points="66,479 317,350 317,479" fill="url(#glow-nebel)"/>
    </svg>
    <div class="brand"><span class="brand__mark"></span>VORTANEL</div>
    <h1 class="title">MUNDSCHUTZ</h1>
    <p class="subtitle">MOUTHGUARD</p>
    <p class="style-name">NEBEL TOR</p>
  </section>

</main>
</body>
</html>
```